Creative Brief
Eastmoor Directorate - Bahrain
Business Cards + Stationary materials.
Simple
Tariq Yousef Al-Mansoori
Head of Financial Affairs
P.O. Box 37182, Awali. Kingdom of Bahrain
talmansoori@eastmoor-dir.example
www.eastmoor-dir.example
We would like the design to include the following colors : cyan, golden & silver. But we are open to new ideas that match our new logo.
Stationary items include :
- A4 letterhead ( would prefer the logo in the top middle section so that we can write the office name on either side of the A4 paper. We would like to use the attached watermark image ( you can change the color to match the theme )
- Notepad
- Presentation folder
- Envelopes ( A4, A3, basically the whole nine yards)
a short explanation on the attached files :
* ED Logo : main logo that represents our office (available in B&W and colored)
* Watermark : design we want as a watermark on the stationary
* Horizon : logo (available in different sizes) that should appear close to the address line and should appear on all stationary materials and business cards. This represents Bahrain horizon plan for economic development, more info can be found here : http://www.horizonplan.example/web/ , or http://wiki.example.org/wiki/Bahrain_Horizon_Plan
We would like to also point out that the back side of the business card MUST include the same information as the front but in Arabic language, you can find the translated info below.
Name : طارق يوسف المنصوري
Title : رئيس الموارد المالية
address :
ص.ب 37182، عوالي. مملكة البحرين
all the other info should be the same.
We wouldn't mind seeing different types of fonts as long as they are professional, serious and formal.
ED Logo : main logo that represents our office - in black and white
ED Logo : main logo that represents our office - colored
design we want as a watermark on the stationary
logo that should appear close to the address line and should appear on all stationary materials and business cards. This represents Bahrain horizon plan for economic development, more info can be found here : http://www.horizonplan.example/web/ ,or http://wiki.example.org/wiki/Bahrain_Horizon_Plan

```html
<!DOCTYPE html>
<html lang="en">
<head>
<meta charset="utf-8">
<title>Eastmoor Directorate – Stationery Set</title>
<link rel="stylesheet" href="https://fonts.googleapis.com/css2?family=Lato:wght@400;700&display=swap">
<style>
  :root{
    --backdrop:#ecebe8;
    --paper:#ffffff;
    --edge:#d9d9d9;
    --blue:#1f3f8f;
    --gold:#b39a5c;
    --gold-light:#d3c190;
    --silver:#e6e8ec;
    --ink:#2a2f3a;
  }
  html,body{margin:0;padding:0;overflow:hidden;background:var(--backdrop);}
  .canvas{display:block;width:1200px;height:348px;font-family:"Lato",sans-serif;}
  .paper{fill:var(--paper);stroke:var(--edge);stroke-width:.6;}
  .band-blue{fill:var(--blue);}
  .band-gold{fill:var(--gold);}
  .band-gold-light{fill:var(--gold-light);}
  .mark-dot{fill:none;stroke:var(--blue);stroke-width:1.2;}
  .brand-name{fill:var(--blue);font-weight:700;font-family:"Lato",sans-serif;}
  .small-text{fill:var(--ink);font-family:"Lato",sans-serif;}
  .arabic-text{fill:var(--ink);font-family:"Lato",sans-serif;}
  .white-text{fill:#fff;font-family:"Lato",sans-serif;}
  .watermark{fill:var(--silver);}
  .slot{fill:var(--blue);}
</style>
</head>
<body>
<svg class="canvas" viewBox="0 0 1200 348" xmlns="http://www.w3.org/2000/svg">

  <!-- Presentation folder -->
  <g class="folder">
    <rect class="paper" x="12" y="12" width="264" height="280"/>
    <path class="band-blue" d="M12 205 Q140 182 276 198 V252 H12Z"/>
    <path class="band-gold" d="M12 248 Q150 230 276 244 V292 H12Z"/>
    <path class="paper" d="M12 252 Q140 236 276 248 V256 Q150 244 12 260Z"/>
    <g class="folder-brand">
      <circle class="mark-dot" cx="180" cy="40" r="9"/>
      <text class="brand-name" x="180" y="68" font-size="9" text-anchor="middle">Eastmoor Directorate</text>
    </g>
    <text class="small-text" x="60" y="160" font-size="4.5" text-anchor="middle">P.O. Box 37182, Awali</text>
    <text class="small-text" x="60" y="166" font-size="4.5" text-anchor="middle">Kingdom of Bahrain</text>
    <text class="small-text" x="232" y="184" font-size="4.5" text-anchor="middle">www.eastmoor-dir.example</text>
    <!-- pocket flaps -->
    <path class="band-gold" d="M12 292 H276 V340 H200 L180 312 H110 L90 340 H12Z"/>
    <path class="paper" d="M110 312 H180 L200 340 H90Z"/>
    <rect class="slot" x="34" y="300" width="44" height="24" rx="2"/>
    <text class="white-text" x="56" y="314" font-size="4" text-anchor="middle">Eastmoor Directorate</text>
    <text class="small-text" x="150" y="328" font-size="5" text-anchor="middle">Horizon</text>
  </g>

  <!-- Business cards, left pair -->
  <g class="card card-front" transform="translate(456 150)">
    <rect class="paper" width="72" height="41"/>
    <circle class="mark-dot" cx="62" cy="8" r="3.5"/>
    <text class="brand-name" x="68" y="16" font-size="2.8" text-anchor="end">Eastmoor Directorate</text>
    <text class="small-text" x="5" y="23" font-size="3.4">Tariq Yousef Al-Mansoori</text>
    <text class="small-text" x="5" y="27.5" font-size="2.8">Head of Financial Affairs</text>
    <path class="band-blue" d="M0 32 Q36 27 72 31 V41 H0Z"/>
  </g>
  <g class="card card-back" transform="translate(540 150)">
    <rect class="paper" width="72" height="41"/>
    <circle class="mark-dot" cx="10" cy="8" r="3.5"/>
    <text class="brand-name" x="4" y="16" font-size="2.8">Eastmoor Directorate</text>
    <text class="arabic-text" x="68" y="23" font-size="3.4" text-anchor="end">طارق يوسف المنصوري</text>
    <text class="arabic-text" x="68" y="27.5" font-size="2.8" text-anchor="end">رئيس الموارد المالية</text>
    <path class="band-gold" d="M0 32 Q36 27 72 31 V41 H0Z"/>
  </g>

  <!-- DL envelope, left -->
  <g class="envelope" transform="translate(456 200)">
    <rect class="paper" width="164" height="68"/>
    <circle class="mark-dot" cx="18" cy="12" r="5"/>
    <text class="brand-name" x="26" y="14" font-size="4.5">Eastmoor Directorate</text>
    <path class="band-blue" d="M0 52 Q80 44 164 50 V60 Q80 54 0 62Z"/>
    <path class="band-gold" d="M0 62 Q80 54 164 60 V68 H0Z"/>
  </g>

  <!-- Letterhead 1 -->
  <g class="letterhead" transform="translate(648 140)">
    <rect class="paper" width="132" height="187"/>
    <circle class="mark-dot" cx="66" cy="12" r="5"/>
    <text class="brand-name" x="66" y="24" font-size="4.5" text-anchor="middle">Eastmoor Directorate</text>
    <rect class="watermark" x="26" y="70" width="80" height="40" rx="6" role="img" aria-label="Faint directorate watermark artwork"/>
    <path class="band-blue" d="M0 170 Q66 160 132 166 V176 Q66 170 0 178Z"/>
    <path class="band-gold" d="M0 178 Q66 170 132 176 V187 H0Z"/>
  </g>

  <!-- Letterhead 2 -->
  <g class="letterhead" transform="translate(828 140)">
    <rect class="paper" width="132" height="187"/>
    <circle class="mark-dot" cx="66" cy="12" r="5"/>
    <text class="brand-name" x="66" y="24" font-size="4.5" text-anchor="middle">Eastmoor Directorate</text>
    <rect class="watermark" x="26" y="70" width="80" height="40" rx="6" role="img" aria-label="Faint directorate watermark artwork"/>
    <path class="band-blue" d="M0 170 Q66 160 132 166 V176 Q66 170 0 178Z"/>
    <path class="band-gold" d="M0 178 Q66 170 132 176 V187 H0Z"/>
  </g>

  <!-- Business cards, right pair -->
  <g class="card card-front" transform="translate(996 150)">
    <rect class="paper" width="72" height="41"/>
    <circle class="mark-dot" cx="62" cy="8" r="3.5"/>
    <text class="brand-name" x="68" y="16" font-size="2.8" text-anchor="end">Eastmoor Directorate</text>
    <text class="small-text" x="5" y="23" font-size="3.4">Tariq Yousef Al-Mansoori</text>
    <text class="small-text" x="5" y="27.5" font-size="2.8">Head of Financial Affairs</text>
    <path class="band-gold" d="M0 32 Q36 27 72 31 V41 H0Z"/>
  </g>
  <g class="card card-back" transform="translate(1074 150)">
    <rect class="paper" width="72" height="41"/>
    <circle class="mark-dot" cx="10" cy="8" r="3.5"/>
    <text class="brand-name" x="4" y="16" font-size="2.8">Eastmoor Directorate</text>
    <text class="arabic-text" x="68" y="23" font-size="3.4" text-anchor="end">طارق يوسف المنصوري</text>
    <text class="arabic-text" x="68" y="27.5" font-size="2.8" text-anchor="end">ص.ب 37182، عوالي</text>
    <path class="band-blue" d="M0 32 Q36 27 72 31 V41 H0Z"/>
  </g>

  <!-- DL envelope, right -->
  <g class="envelope" transform="translate(996 204)">
    <rect class="paper" width="156" height="66"/>
    <circle class="mark-dot" cx="18" cy="12" r="5"/>
    <text class="brand-name" x="26" y="14" font-size="4.5">Eastmoor Directorate</text>
    <path class="band-gold-light" d="M0 50 Q78 42 156 48 V58 Q78 52 0 60Z"/>
    <path class="band-gold" d="M0 60 Q78 52 156 58 V66 H0Z"/>
  </g>

</svg>
</body>
</html>
```